Striking Business Card for Exotic Car Ministry

Design a striking business card that will motivate people to go to the website. I want this card to be unique but readable. We use exotic cars to minister to people on Viewtube as well as car shows. I would like the background to be black and high impact.

This is the craziest thing, a minimum of 300 words? How do you make something so simple, so difficult to complete? I guess I will just continue to type until I get the necessary three hundred words. No, not even close now, so I continue typing. Christmas is nearing and may be here before I achieve this silly goal of three hundred words. They may as well ask for one thousand words as it would be similarly insane. It would even be helpful to know my word count.

Target Market(s)

Men

Industry/Entity Type

Automotive

Contact Information for Business Card

Logo with Ministry & Outreach nearby to describe service. Include Ravenfall42.com and Doug@Ravenfall42.com somewhere on card. Bullet points: Viewtube, Car Shows, Forum, Outreach...Include: Watch Videos on Viewtube logo.

On the rear of the card: Commit your work to the Lord, and your plans will succeed. Proverbs 16:3

There will be no telephone number. Include image of 2017 Velcor TRZ on the front.

Colors

Designer to choose colors to be used in the design.

Requirements
Must have
• Card should be a dark color like black or gray. Must not be a traditional boring card.
Nice to have
• I think this describes it well.
Should not have
• I wouldnt expect any questions.

```html
<!DOCTYPE html>
<html lang="en">
<head>
<meta charset="utf-8">
<title>Ravenfall Business Card</title>
<link href="https://fonts.googleapis.com/css2?family=Michroma&family=Oswald:wght@500&family=Work+Sans:ital,wght@0,400;1,400&display=swap" rel="stylesheet">
<style>
  :root {
    --page-bg: #4a4239;
    --card-black: #000;
    --ink-white: #f4f4f4;
    --accent-red: #e3232b;
    --photo-light: #c9c9c9;
    --photo-mid: #6e6e6e;
  }
  * { margin: 0; padding: 0; box-sizing: border-box; }
  html, body { width: 1200px; height: 930px; overflow: hidden; }
  body { background: var(--page-bg); position: relative; font-family: "Work Sans", sans-serif; }

  .card {
    position: absolute;
    left: 278px;
    width: 644px;
    height: 368px;
    border-radius: 24px;
    background: var(--card-black);
    overflow: hidden;
    color: var(--ink-white);
  }
  .card--front { top: 76px; }
  .card--back { top: 486px; }

  .car-photo { position: absolute; }
  .card--front .car-photo {
    left: 190px; top: 110px; width: 454px; height: 258px;
    background: radial-gradient(ellipse 60% 55% at 60% 50%, var(--photo-light) 0%, var(--photo-mid) 55%, rgba(0,0,0,0) 100%);
  }
  .card--back .car-photo {
    left: 0; top: 50px; width: 644px; height: 250px;
    background: radial-gradient(ellipse 55% 50% at 55% 50%, #5a5a5a 0%, #2c2c2c 55%, rgba(0,0,0,0) 100%);
  }

  .brand-name {
    position: absolute;
    font-family: "Michroma", sans-serif;
    color: var(--ink-white);
    letter-spacing: 1px;
    white-space: nowrap;
  }
  .card--front .brand-name { left: 24px; top: 48px; font-size: 30px; }
  .card--back .brand-name { left: 0; right: 0; top: 140px; text-align: center; font-size: 52px; }

  .watch-line {
    position: absolute; left: 24px; top: 118px;
    display: flex; align-items: center; gap: 18px;
    font-size: 15px; color: var(--accent-red);
  }
  .channel-name { display: flex; align-items: center; gap: 5px; color: var(--ink-white); font-size: 14px; }
  .channel-name::after { content: ""; width: 10px; height: 10px; background: var(--accent-red); }

  .service-list {
    position: absolute; left: 24px; top: 171px;
    list-style: none;
    font-family: "Michroma", sans-serif;
    font-size: 14px; line-height: 21.3px;
  }
  .service-list li { display: flex; align-items: center; gap: 13px; }
  .service-list li::before {
    content: ""; width: 10px; height: 10px; border-radius: 50%; background: var(--accent-red);
  }

  .contact {
    position: absolute; left: 26px; top: 290px;
    font-style: italic; font-size: 17px; line-height: 22px; letter-spacing: 0.5px;
  }

  .verse {
    position: absolute; left: 34px; right: 34px; top: 319px;
    text-align: center;
    white-space: nowrap;
    font-family: "Oswald", sans-serif; font-weight: 500;
    font-size: 17px; letter-spacing: 0;
    text-transform: uppercase;
    color: var(--ink-white);
  }
</style>
</head>
<body>

  <section class="card card--front">
    <div class="car-photo" role="img" aria-label="Photo of a silver 2017 Velcor TRZ sports car"></div>
    <div class="brand-name">RAVENFALL</div>
    <div class="watch-line">
      <span>Watch Videos on Viewtube</span>
      <span class="channel-name">Viewtube</span>
    </div>
    <ul class="service-list">
      <li>VIEWTUBE</li>
      <li>CAR</li>
      <li>SHOWS</li>
      <li>FORUM</li>
      <li>OUTREACH</li>
    </ul>
    <div class="contact">
      <div>Doug@Ravenfall42.com</div>
      <div>www.Ravenfall42.com</div>
    </div>
  </section>

  <section class="card card--back">
    <div class="car-photo" role="img" aria-label="Faint dark photo of the Velcor TRZ sports car"></div>
    <div class="brand-name">RAVENFALL</div>
    <p class="verse">Commit your work to the Lord, and your plans will succeed. Proverbs 16:3</p>
  </section>

</body>
</html>
```